Flyer Mail out

Need something urgently designed.

I need a flyer done double sided I have provided CWDG photos and the writing. I do not have any dental surgery stock photos as such but this can be used. We are a mobile dental company that goes out to schools and provide free dental services.

I have attached the written document and would like it double sided A4 paper.

The colours I want is Aqua, Light Blue, dark blue, grey and white.

Just need it designed beautifully and professionally to go out to principals to contact us and use our services.

If you would like more info have a look at our Chatterloop page Coastline Wandering Dental Group

```html
<!DOCTYPE html>
<html lang="en">
<head>
<meta charset="utf-8">
<title>CWDG Flyer – Dear Principal</title>
<link href="https://fonts.googleapis.com/css2?family=Roboto+Condensed:wght@300;400;700&display=swap" rel="stylesheet">
<style>
  :root {
    --aqua: #52c1d7;
    --aqua-light: #82d2e2;
    --photo-tone: #8fd3e2;
    --photo-tone-dark: #5fb6c9;
    --grey: #7e8d93;
    --grey-dark: #6f7e84;
    --white: #ffffff;
    --muted: #b9e6ef;
  }
  * { margin: 0; padding: 0; box-sizing: border-box; }
  html, body { width: 1200px; height: 848px; overflow: hidden; background: var(--white); }
  body { font-family: "Roboto Condensed", "Arial Narrow", sans-serif; }
  .flyer { position: relative; width: 1200px; height: 848px; }

  /* Left side */
  .team-photo {
    position: absolute; left: 0; top: 152px; width: 601px; height: 462px;
    background: linear-gradient(160deg, var(--photo-tone) 0%, var(--photo-tone-dark) 100%);
  }
  .booking { position: absolute; left: 36px; top: 648px; color: var(--grey); }
  .booking-lead { font-weight: 300; font-size: 19px; line-height: 23px; letter-spacing: 0.2px; text-transform: uppercase; }
  .booking-headline { margin-top: 6px; font-weight: 700; font-size: 55px; line-height: 52px; letter-spacing: 0.5px; color: var(--grey-dark); }
  .booking-headline .bang { font-weight: 300; }

  /* Right side */
  .letter { position: absolute; left: 632px; top: 0; width: 568px; height: 848px; background: var(--aqua); color: var(--white); }
  .letter-intro { position: absolute; left: 35px; top: 38px; width: 500px; }
  .heading { font-weight: 700; font-size: 34px; line-height: 36px; }
  .heading .light { font-weight: 400; }
  .intro-text { margin-top: 12px; font-size: 9.6px; line-height: 12.5px; }
  .intro-text p + p { margin-top: 11px; }
  .offer-heading { position: absolute; left: 35px; top: 242px; }

  .offers { position: absolute; left: 0; top: 284px; width: 568px; height: 366px; background: var(--aqua-light); }
  .offer { position: absolute; width: 160px; text-align: center; }
  .offer svg { display: block; margin: 0 auto; height: 40px; width: 44px; }
  .offer-title { margin-top: 14px; font-weight: 700; font-size: 9.6px; line-height: 12px; text-transform: uppercase; }
  .offer-text { margin-top: 18px; font-size: 9.6px; line-height: 12.5px; }
  .offer-1 { left: 33px; top: 31px; }
  .offer-2 { left: 204px; top: 31px; }
  .offer-3 { left: 376px; top: 31px; }
  .offer-4 { left: 116px; top: 200px; }
  .offer-5 { left: 289px; top: 200px; }

  .closing { position: absolute; left: 35px; top: 668px; width: 500px; font-size: 9.6px; line-height: 12.5px; }
  .closing p + p { margin-top: 12px; }
  .closing strong { font-weight: 700; }
  .closing .note { color: var(--muted); }
</style>
</head>
<body>
<div class="flyer">

  <div class="team-photo" role="img" aria-label="Photo of the dental team in scrubs standing in front of the mobile dental clinic truck, tinted aqua"></div>

  <div class="booking">
    <p class="booking-lead">Book us now for 2015 and<br>help us bring back your student’s</p>
    <p class="booking-headline">BRIGHT SMILE<span class="bang">!</span></p>
  </div>

  <section class="letter">
    <div class="letter-intro">
      <h1 class="heading">Dear Principal<span class="light">,</span></h1>
      <div class="intro-text">
        <p>We thank you for the time you are taking to review our mobile dental service. Here at Coastline Wandering Dental Group (CWDG), we are committed to ‘bringing the dentist to you’.</p>
        <p>We are passionate about providing Bulked Billed Oral Health Care to Primary and High Schools, Aged Care Facilities, Corporate Companies and Aboriginal Communities. Within New South Wales, in the past year, we have serviced <strong>over 150 schools</strong>, and treated a total of <strong>22,014 students</strong> so far.</p>
        <p>We are pleased to introduce our service designed to satisfy your student’s dental needs. Our service is cost effective, user friendly and extremely beneficial in providing oral health education and prevention.</p>
      </div>
    </div>

    <h2 class="heading offer-heading">We offer<span class="light">:</span></h2>

    <div class="offers">
      <div class="offer offer-1">
        <svg viewBox="0 0 44 40" aria-hidden="true"><path fill="#fff" d="M22 38 C10 28 2 21 2 12 C2 6 7 2 12 2 C16 2 20 4 22 8 C24 4 28 2 32 2 C37 2 42 6 42 12 C42 21 34 28 22 38 Z"/></svg>
        <p class="offer-title">Free bulk-billed<br>assessment and treatment</p>
        <p class="offer-text">Students who qualify for Healthcover “Bright Start Smiles” program get a dental check-up, cleaning &amp; fluoride treatment, sealants, X-rays and fillings.</p>
      </div>
      <div class="offer offer-2">
        <svg viewBox="0 0 44 40" aria-hidden="true"><ellipse cx="17" cy="15" rx="15" ry="11" fill="#fff"/><path fill="#fff" d="M8 23 L5 31 L15 25 Z"/><ellipse cx="29" cy="22" rx="13" ry="10" fill="#fff" stroke="#82d2e2" stroke-width="2"/><path fill="#fff" d="M36 29 L40 36 L31 31 Z"/></svg>
        <p class="offer-title">One-on-one<br>oral health education</p>
        <p class="offer-text">Get one-on-one oral health education from our professional dentists and oral health therapists that will help you on your dental care!</p>
      </div>
      <div class="offer offer-3">
        <svg viewBox="0 0 44 40" aria-hidden="true"><g fill="none" stroke="#fff" stroke-width="2.5" stroke-linejoin="round"><path d="M8 16 L22 21 L36 16 L36 34 L22 38 L8 34 Z"/><path d="M22 21 L22 38"/><path d="M8 16 L3 9 L17 4 L22 11 L27 4 L41 9 L36 16"/><path d="M22 11 L8 16 M22 11 L36 16"/></g></svg>
        <p class="offer-title">Complimentary<br>dental care pack</p>
        <p class="offer-text">Win a complimentary dental care pack, comprising of a toothbrush, toothpaste and some other products.</p>
      </div>
      <div class="offer offer-4">
        <svg viewBox="0 0 44 40" aria-hidden="true"><path fill="#fff" d="M15 22 L9 38 L14 35 L17 39 L21 26 Z M29 22 L35 38 L30 35 L27 39 L23 26 Z"/><circle cx="22" cy="14" r="12" fill="#fff"/><circle cx="22" cy="14" r="8.5" fill="none" stroke="#82d2e2" stroke-width="1.5"/><text x="22" y="18.5" text-anchor="middle" font-family="Roboto Condensed, sans-serif" font-weight="700" font-size="12" fill="#82d2e2">1</text></svg>
        <p class="offer-title">Win various<br>prices drawns</p>
        <p class="offer-text">Students also go into the draw to win various prices drawn after the clinic’s visit to the school.</p>
      </div>
      <div class="offer offer-5">
        <svg viewBox="0 0 44 40" aria-hidden="true"><g fill="none" stroke="#fff" stroke-width="2.5" stroke-linejoin="round"><rect x="9" y="5" width="26" height="33" rx="2"/><rect x="16" y="2" width="12" height="6" rx="1" fill="#fff"/><path d="M15 23 L21 30 L34 14" stroke-width="4" stroke-linecap="round"/></g></svg>
        <p class="offer-title">Referral to your<br>regular dentist</p>
        <p class="offer-text">Provide a referral to the student’s regular dentist for further treatment they may require.</p>
      </div>
    </div>

    <div class="closing">
      <p>CWDG operates within accepted best practice models, and as such, is familiar, and without exception complies with the relevant legislation, regulations, codes and guidelines governing dentistry, including but not limited to, the <strong>Dental Code of Conduct for Health Practitioners by the Dental Practice Council</strong>.</p>
      <p>Our mobile dental clinics feature state-of-the-art, oral health equipment and machinery, including a Dental X-Ray OPG that features low dose radiation, as well as Child Safety Standard Wheel Chair Access.<br><span class="note">(Please see our website for more information)</span></p>
      <p><strong>Thank you for considering CWDG, my team and I look forward to providing this free service to your school and most importantly, ‘bringing the dentist to you’.</strong></p>
    </div>
  </section>

</div>
</body>
</html>
```